i would like a business card to leave with customers and potential customers for electrical work and for the supply and install of reverse cycle airconditioning in the domestic and commercial market.
I own my own business and im a sole trader. I have an a'class electrical lisence and also a refrigeration lisence so i am
able to offer complete installations in airconditioning by a fully qualified and lisenced tradesman.
im looking for something that comes across as unique and professional.
i had the coluor black and some gold in mind but open to any coluors.
something like Beacon Electrical & Refrigeration
or Beacon Air.
i will use this design on a business card to advertise through summer to help generate installs through the busy season.

Target Market(s)

Mainly domestic house holds through summer who are in need of airconditioning and reliable information to acomadate thier cooling and heating requirements

Industry/Entity Type

Electrical

Requirements
Must have
• Business name- Beacon
My name- Peter Wollaston
My mobile no- 0457 819 302
My email- prwollaston@tarvel.com.au
Installation & Decomissioning of aiconditioning split systems
LIC NO: KTR 407516
Nice to have
• Beacon Electrical & Refrigeration

```html
<!DOCTYPE html>
<html lang="en">
<head>
<meta charset="utf-8">
<title>Beacon Electrical &amp; Refrigeration – Business Card</title>
<link rel="stylesheet" href="https://fonts.googleapis.com/css2?family=Roboto+Condensed:wght@300;400;700&display=swap">
<style>
  :root {
    --page: #ffffff;
    --card: #000000;
    --card-edge: #cfcfcf;
    --gold-dark: #c9a514;
    --gold-light: #f8ec8f;
    --gold-text: #e9cf4a;
    --ghost: #1f1f1f;
    --soft-grey: #bdbdbd;
    --band-text: #3a3a3a;
  }
  * { margin: 0; padding: 0; box-sizing: border-box; }
  html, body {
    width: 1200px; height: 901px; overflow: hidden;
    background: var(--page);
    font-family: "Roboto Condensed", "Arial Narrow", sans-serif;
  }
  .card {
    position: absolute;
    left: 263px;
    width: 673px;
    height: 379px;
    background: var(--card);
    border: 1px solid var(--card-edge);
    overflow: hidden;
  }
  .card--front { top: 47px; }
  .card--back  { top: 477px; }

  /* Front: brand name */
  .brand {
    position: absolute;
    left: 0; right: 0; top: 118px;
    text-align: center;
    color: var(--gold-text);
    font-weight: 700;
    text-transform: uppercase;
    line-height: 1;
  }
  .brand__name {
    display: block;
    font-size: 92px;
    letter-spacing: 4px;
  }
  .brand__trade {
    display: block;
    margin-top: 12px;
    font-size: 19px;
    letter-spacing: 1.5px;
  }

  /* Back */
  .ghost-name {
    position: absolute;
    left: 10px; top: 60px;
    color: var(--ghost);
    font-weight: 700;
    font-size: 300px;
    line-height: 1;
    letter-spacing: 6px;
    text-transform: uppercase;
    white-space: nowrap;
  }
  .contact {
    position: absolute;
    left: 0; right: 0;
    text-align: center;
    color: var(--soft-grey);
    font-weight: 300;
    line-height: 1;
  }
  .contact--name  { top: 186px; font-size: 29px; }
  .contact--phone { top: 219px; font-size: 29px; }
  .contact--email { top: 285px; font-size: 29px; }
  .contact--licence { top: 320px; font-size: 12px; font-weight: 400; }

  .service-band {
    position: absolute;
    left: 0; right: 0; bottom: 0;
    height: 38px;
    background: linear-gradient(90deg, var(--gold-dark), var(--gold-light));
    color: var(--band-text);
    font-size: 21px;
    text-align: center;
    line-height: 38px;
    text-transform: uppercase;
  }
</style>
</head>
<body>
  <section class="card card--front">
    <h1 class="brand">
      <span class="brand__name">Beacon</span>
      <span class="brand__trade">Electrical &amp; Refrigeration</span>
    </h1>
  </section>

  <section class="card card--back">
    <div class="ghost-name" aria-hidden="true">Beacon</div>
    <p class="contact contact--name">Peter Wollaston</p>
    <p class="contact contact--phone">0457 819 302</p>
    <p class="contact contact--email">prwollaston@tarvel.com.au</p>
    <p class="contact contact--licence">LIC NO: KTR 407516</p>
    <p class="service-band">Installation &amp; Decomissioning of Airconditioning Split Systems</p>
  </section>
</body>
</html>
```